Executive search firm in fashion, luxury and retail industry needs logo and card design.

We are a start-up recruiting firm that specializes in the retail and fashion industry, based in New York. We are looking for something that will appeal to CEO level clients and candidates, but that has a little design edge...not overly corporate but still CEO-appropriate. We have clean, sophisticated taste and want a contemporary feel. Happy to have a two sided card. Not afraid of a little color but it should be high-design, not gimmicky and tasteful.

Quillmart Market(s)

CEO's, HR Leaders, in retail, fashion (i.e. Halvorsen, Quillmart, Otto Brevik)

Industry/Entity Type

Professional Service

Contact Information for Business Card

Calloway Ridge Search Partners
Address to be determined
Larkspur, NY 00000

Marta Velard
Managing Director
(555)038-4172
mvelard@callowayridgesearch.example

Font styles to use
Serif
Sans Serif

Requirements
Must have
• clean lines, crisp graphics, some color. Prefer a graphic treatment over a "logo" per se. No pictures, etc.
Nice to have
• double sided design.
Should not have
• Gimmicks, smaltz, goop. Think Gallery of Current Works, not the Dunmore Holdings. No earth tones, as in beige and brown, no pastels. Strong colors are fine in moderation. Grays are good. Jewel tones are good. No red.

```html
<!DOCTYPE html>
<html lang="en">
<head>
<meta charset="utf-8">
<title>Calloway Ridge Search Partners – Business Card</title>
<link rel="stylesheet" href="https://fonts.googleapis.com/css2?family=Open+Sans:wght@400;600&family=Raleway:wght@500;600&display=swap">
<style>
  :root {
    --backdrop: #e9e7e4;
    --card-white: #ffffff;
    --band-grey: #8b8b8b;
    --brand-grey: #8a8a8a;
    --accent-yellow: #f0c419;
    --divider-grey: #c9c9c9;
    --text-white: #ffffff;
    --shadow: rgba(0, 0, 0, 0.18);
  }
  html, body {
    margin: 0;
    padding: 0;
    width: 1200px;
    height: 900px;
    overflow: hidden;
    background: var(--backdrop);
    font-family: "Open Sans", Arial, sans-serif;
  }
  .canvas {
    position: relative;
    width: 1200px;
    height: 900px;
  }
  .card {
    position: absolute;
    background: var(--card-white);
    box-shadow: 0 4px 14px var(--shadow);
    overflow: hidden;
  }

  /* Front side */
  .card-front {
    left: 77px;
    top: 34px;
    width: 588px;
    height: 363px;
  }
  .front-header {
    position: absolute;
    left: 0; top: 0;
    width: 100%;
    height: 156px;
  }
  .brand-dot {
    position: absolute;
    left: 52px; top: 54px;
    width: 58px;
    height: 58px;
    border-radius: 50%;
    background: var(--accent-yellow);
  }
  .brand-divider {
    position: absolute;
    left: 177px; top: 38px;
    width: 2px;
    height: 90px;
    background: var(--divider-grey);
  }
  .brand-name {
    position: absolute;
    left: 197px; top: 38px;
    margin: 0;
    color: var(--brand-grey);
    font-family: "Raleway", Arial, sans-serif;
    font-weight: 600;
    text-transform: uppercase;
  }
  .brand-main {
    display: block;
    font-size: 48px;
    line-height: 58px;
    letter-spacing: 1px;
  }
  .brand-sub {
    display: block;
    font-size: 19px;
    line-height: 26px;
    letter-spacing: 0.3px;
  }
  .front-band {
    position: absolute;
    left: 0; top: 156px;
    width: 100%;
    height: 207px;
    background: var(--band-grey);
    color: var(--text-white);
  }
  .contact-name {
    position: absolute;
    left: 32px; top: 30px;
    margin: 0;
    font-size: 19px;
    font-weight: 600;
  }
  .contact-title {
    position: absolute;
    left: 32px; top: 56px;
    margin: 0;
    font-size: 15px;
  }
  .contact-city {
    position: absolute;
    left: 31px; top: 93px;
    margin: 0;
    font-size: 15px;
  }
  .contact-list {
    position: absolute;
    left: 32px; top: 131px;
    margin: 0;
    padding: 0;
    list-style: none;
    font-size: 15px;
  }
  .contact-list li {
    display: flex;
    align-items: center;
    height: 25px;
  }
  .contact-icon {
    width: 13px;
    height: 13px;
    margin-right: 14px;
    fill: var(--text-white);
  }

  /* Back side */
  .card-back {
    left: 388px;
    top: 505px;
    width: 567px;
    height: 352px;
  }
  .back-band {
    position: absolute;
    left: 0; top: 110px;
    width: 100%;
    height: 130px;
    background: var(--band-grey);
    display: flex;
    align-items: center;
    justify-content: center;
  }
  .back-brand-name {
    margin: 0;
    color: var(--text-white);
    font-family: "Raleway", Arial, sans-serif;
    font-weight: 500;
    text-align: center;
    text-transform: uppercase;
  }
  .back-brand-name .brand-main {
    font-size: 60px;
    line-height: 70px;
    letter-spacing: 2px;
  }
  .back-brand-name .brand-sub {
    font-size: 23px;
    line-height: 30px;
    letter-spacing: 0.3px;
  }
</style>
</head>
<body>
<main class="canvas">

  <section class="card card-front" aria-label="Business card front">
    <header class="front-header">
      <span class="brand-dot" aria-hidden="true"></span>
      <span class="brand-divider" aria-hidden="true"></span>
      <p class="brand-name">
        <span class="brand-main">Calloway</span>
        <span class="brand-sub">Ridge Search Partners</span>
      </p>
    </header>
    <div class="front-band">
      <h1 class="contact-name">Marta Velard</h1>
      <p class="contact-title">Managing Director</p>
      <p class="contact-city">Larkspur, NY 00000</p>
      <ul class="contact-list">
        <li>
          <svg class="contact-icon" viewBox="0 0 24 24" aria-hidden="true"><path d="M6.6 10.8a15.2 15.2 0 0 0 6.6 6.6l2.2-2.2a1 1 0 0 1 1-.25 11.4 11.4 0 0 0 3.6.57 1 1 0 0 1 1 1V20a1 1 0 0 1-1 1A17 17 0 0 1 3 4a1 1 0 0 1 1-1h3.5a1 1 0 0 1 1 1c0 1.250.2 2.45.57 3.57a1 1 0 0 1-.25 1z"/></svg>
          (555)038-4172
        </li>
        <li>
          <svg class="contact-icon" viewBox="0 0 24 24" aria-hidden="true"><path d="M2 5h20v14H2z M3.5 6.5v.3L12 12.5l8.5-5.7v-.3z" fill-rule="evenodd"/></svg>
          mvelard@callowayridgesearch.example
        </li>
      </ul>
    </div>
  </section>

  <section class="card card-back" aria-label="Business card back">
    <div class="back-band">
      <p class="back-brand-name">
        <span class="brand-main">Calloway</span>
        <span class="brand-sub">Ridge Search Partners</span>
      </p>
    </div>
  </section>

</main>
</body>
</html>
```